Mesa Bloom

We have opened new business that includes pottery & chimineas we want cards to have collage of pictures of products on front of card then information on back. On back in middle MESA BLOOM +
marlo_tesh@fernmail.example
(555) 318-2274
(555)3182917 & mesabloom@fernmail.example
Business
Sans Serif
Decorative

```html
<!DOCTYPE html>
<html lang="en">
<head>
<meta charset="utf-8">
<title>Mesa Bloom – Business Card</title>
<link rel="stylesheet" href="https://fonts.googleapis.com/css2?family=Arimo:wght@400;700&display=swap">
<style>
  :root {
    --backdrop: #cfcfcf;
    --backdrop-light: #e4e4e4;
    --card-white: #fbfbfb;
    --ink: #2b2b2b;
    --band: #b97cb1;
    --clay-brown: #8a5134;
    --clay-rust: #a4623f;
    --glaze-green: #4f6f55;
    --glaze-sage: #7d8d63;
    --glaze-teal: #5f9e97;
    --glaze-slate: #4a4d52;
    --glaze-blue: #6f8fa8;
    --shed-shadow: #5b4a3f;
  }
  * { box-sizing: border-box; margin: 0; padding: 0; }
  html, body { width: 1200px; height: 800px; overflow: hidden; }
  body {
    background: radial-gradient(ellipse at 50% 20%, var(--backdrop-light), var(--backdrop) 70%);
    font-family: "Arimo", Arial, sans-serif;
    color: var(--ink);
    position: relative;
  }
  .card {
    position: absolute;
    top: 245px;
    width: 540px;
    height: 310px;
    background: var(--card-white);
    box-shadow: 0 6px 18px rgba(0,0,0,0.18);
    overflow: hidden;
  }
  .card--front { left: 40px; }
  .card--back { left: 620px; }

  /* Front: product collage */
  .collage {
    position: absolute; inset: 0;
    display: grid;
    grid-template-columns: 1.3fr 1.1fr 0.9fr 1.1fr;
    grid-template-rows: 1fr 1fr;
    gap: 4px;
    background: var(--card-white);
  }
  .collage__tile { width: 100%; height: 100%; }
  .tile--yard { grid-column: 1; grid-row: 1; background: linear-gradient(160deg, var(--glaze-blue), var(--clay-rust) 50%, var(--glaze-green)); }
  .tile--vases { grid-column: 1; grid-row: 2; background: linear-gradient(170deg, #6a4a3a, var(--clay-brown) 45%, var(--glaze-green) 85%); }
  .tile--urns { grid-column: 2; grid-row: 1; background: linear-gradient(180deg, #d9d6d0, var(--glaze-slate) 70%); }
  .tile--green-urn { grid-column: 3; grid-row: 1; background: linear-gradient(180deg, #e4d9b8, var(--glaze-sage) 60%, #3a3a32); }
  .tile--teal-vase { grid-column: 4; grid-row: 1 / 3; background: linear-gradient(180deg, #3a2a25, var(--glaze-teal) 35%, #c0614e 75%, var(--glaze-teal)); }
  .tile--shed { grid-column: 2; grid-row: 2; background: linear-gradient(170deg, var(--shed-shadow), var(--clay-brown) 60%, var(--glaze-slate)); }
  .tile--small-urn { grid-column: 3; grid-row: 2; background: linear-gradient(180deg, #e6e6e6, var(--glaze-slate) 55%, #d8d8d8); }

  /* Back: contact info */
  .brand {
    position: absolute; left: 34px; top: 82px;
    display: flex; align-items: center; gap: 14px;
  }
  .brand__mark { width: 14px; height: 14px; background: var(--ink); }
  .brand__text { display: flex; flex-direction: column; gap: 4px; }
  .brand__owners { font-weight: 700; font-size: 28px; letter-spacing: -0.3px; }
  .brand__business { font-size: 15px; font-weight: 700; letter-spacing: 0.3px; }

  .contacts {
    position: absolute; left: 24px; right: 24px; top: 182px;
    display: flex; flex-direction: column; gap: 10px;
  }
  .band {
    background: var(--band);
    height: 32px;
    padding: 0 16px;
    display: flex; align-items: center; justify-content: space-between;
    font-size: 16px;
    white-space: nowrap;
  }
</style>
</head>
<body>
  <section class="card card--front" aria-label="Card front">
    <div class="collage">
      <div class="collage__tile tile--yard" role="img" aria-label="Photo of glazed pottery urns gathered in a yard"></div>
      <div class="collage__tile tile--vases" role="img" aria-label="Photo of carved brown and green vases"></div>
      <div class="collage__tile tile--urns" role="img" aria-label="Photo of two dark slate garden urns"></div>
      <div class="collage__tile tile--green-urn" role="img" aria-label="Photo of a mottled green urn"></div>
      <div class="collage__tile tile--teal-vase" role="img" aria-label="Photo of a tall teal and red vase"></div>
      <div class="collage__tile tile--shed" role="img" aria-label="Photo of pottery stacked in the shop"></div>
      <div class="collage__tile tile--small-urn" role="img" aria-label="Photo of a small dark carved urn"></div>
    </div>
  </section>

  <section class="card card--back" aria-label="Card back">
    <div class="brand">
      <span class="brand__mark" aria-hidden="true"></span>
      <div class="brand__text">
        <span class="brand__owners">Marlo &amp; Dana Tesh</span>
        <span class="brand__business">MESA BLOOM +</span>
      </div>
    </div>
    <div class="contacts">
      <div class="band"><span class="band__email">marlo_tesh@fernmail.example</span><span class="band__phone">(555) 318-2274</span></div>
      <div class="band"><span class="band__email">mesabloom@fernmail.example</span><span class="band__phone">(555) 318-2917</span></div>
    </div>
  </section>
</body>
</html>
```